Fertilizer Company exhibiting products for sale at Hemp Expo Show

Organic fertilizer company exhibiting at a hemp trade show. We have a 10x10 booth. There is no pipe and drape, so we are looking to have a fully custom canopy designed and printed with a backdrop and sides. Please submit designs as if I was looking at a full expo show display - Canopy, backdrop, side walls, tables, etc.

Target Market(s)

Hemp Businesses

Industry/Entity Type

Agriculture, Hemp, Fertilizer

Font styles to use
Sans Serif

Colors
0054AA
0677BA
7BADD7
CADEEF
E8F1F8
0094D4
00A9DD
6FCCEA
C7EBF8
E9F6FB
00AB8E
00BBA5
67D7C9
C6EFE9
E9F9F6
59FF00
82FF00
B8FF75
E3FFCB
F4FFEA
FFF300
FFF600
FEFA6F
FFFEC7
FFFEE8
FFC000
F8CF3A
FAE287
FDF2CF
FEFAEE
F0912C
F2A743
F7CA91
FBE8D2
FDF5EE
EE7325
F08F49
F5BC92
FAE3D3
FDF4ED

Requirements
Must have
• Custom designed canopy that integrates my branding files - Sky & Lightning Bolts, Pell Vantor Logo
Should not have
• Red anywhere. Red in agriculture means dead.

```html
<!DOCTYPE html>
<html lang="en">
<head>
<meta charset="utf-8">
<title>Pell Vantor – Vero Bloom Expo Booth</title>
<link href="https://fonts.googleapis.com/css2?family=Comfortaa:wght@400;700&family=Montserrat:wght@600;700;800&display=swap" rel="stylesheet">
<style>
  :root {
    --canopy-grey: #3b3b3d;
    --canopy-grey-dark: #2c2c2e;
    --cloth-grey: #333335;
    --leaf-green: #6b9a2f;
    --leaf-green-dark: #4f7d26;
    --accent-lime: #b8ff75;
    --accent-yellow: #e3f53a;
    --band-orange: #f0912c;
    --sky-blue: #0094d4;
    --pole-silver: #d9dadc;
    --ceiling-grey: #d4d5d7;
    --text-white: #ffffff;
    --heading-ink: #1d1d1d;
    --page: #ffffff;
  }
  html, body {
    margin: 0;
    padding: 0;
    width: 1200px;
    height: 3030px;
    overflow: hidden;
    background: var(--page);
  }
  .booth-sheet { display: block; width: 1200px; height: 3030px; }
  .brand-name { font-family: "Montserrat", sans-serif; font-weight: 800; fill: var(--text-white); letter-spacing: 1px; }
  .product-name { font-family: "Montserrat", sans-serif; font-weight: 800; fill: var(--text-white); letter-spacing: 1px; }
  .tagline { font-family: "Comfortaa", sans-serif; font-weight: 700; fill: var(--accent-lime); }
  .promise { font-family: "Montserrat", sans-serif; font-weight: 700; fill: var(--text-white); }
  .promise-soft { font-family: "Comfortaa", sans-serif; font-weight: 700; fill: var(--text-white); }
  .promise-accent { font-family: "Comfortaa", sans-serif; font-weight: 700; fill: var(--accent-yellow); }
  .benefit-label { font-family: "Comfortaa", sans-serif; font-weight: 700; fill: var(--text-white); }
  .flag-word { font-family: "Comfortaa", sans-serif; font-weight: 700; fill: var(--canopy-grey); font-size: 12px; }
  .section-heading { font-family: "Montserrat", sans-serif; font-weight: 700; fill: var(--heading-ink); font-size: 24px; }
</style>
</head>
<body>
<svg class="booth-sheet" viewBox="0 0 1200 3030" xmlns="http://www.w3.org/2000/svg">
  <defs>
    <linearGradient id="roofShade" x1="0" y1="0" x2="0" y2="1">
      <stop offset="0" stop-color="#4a4b4f"/>
      <stop offset="1" stop-color="#333436"/>
    </linearGradient>
    <linearGradient id="fieldPhoto" x1="0" y1="0" x2="1" y2="1">
      <stop offset="0" stop-color="#6f9e32"/>
      <stop offset="0.55" stop-color="#4f7d26"/>
      <stop offset="1" stop-color="#2f4f17"/>
    </linearGradient>
    <radialGradient id="treeGlow" cx="0.5" cy="0.5" r="0.5">
      <stop offset="0" stop-color="#a6d84a"/>
      <stop offset="0.6" stop-color="#7fb23a"/>
      <stop offset="1" stop-color="#6b9a2f" stop-opacity="0"/>
    </radialGradient>
    <linearGradient id="floorShade" x1="0" y1="0" x2="0" y2="1">
      <stop offset="0" stop-color="#e4e5e7"/>
      <stop offset="1" stop-color="#ffffff"/>
    </linearGradient>
  </defs>

  <!-- ===== Scene one: full booth front ===== -->
  <g class="booth-front">
    <!-- roof -->
    <path d="M205,314 Q470,200 597,58 Q724,200 989,314 Z" fill="url(#roofShade)"/>
    <circle cx="428" cy="240" r="16" fill="var(--leaf-green)"/>
    <text class="brand-name" x="452" y="253" font-size="34">PELL VANTOR</text>

    <!-- valance -->
    <rect x="205" y="314" width="784" height="8" fill="var(--band-orange)"/>
    <rect x="205" y="322" width="784" height="34" fill="var(--leaf-green)"/>
    <rect x="205" y="356" width="784" height="30" fill="var(--canopy-grey)"/>
    <text class="product-name" x="284" y="356" font-size="27">VERO BLOOM</text>
    <text class="tagline" x="275" y="374" font-size="15">fast growth | vigorous roots | performance boost</text>

    <!-- floor and legs -->
    <rect x="215" y="735" width="770" height="100" fill="url(#floorShade)"/>
    <rect x="207" y="386" width="7" height="452" fill="var(--pole-silver)"/>
    <rect x="980" y="386" width="7" height="452" fill="var(--pole-silver)"/>
    <rect x="300" y="386" width="6" height="350" fill="var(--pole-silver)"/>
    <rect x="886" y="386" width="6" height="350" fill="var(--pole-silver)"/>
    <rect x="202" y="836" width="18" height="4" fill="var(--canopy-grey-dark)"/>
    <rect x="975" y="836" width="18" height="4" fill="var(--canopy-grey-dark)"/>

    <!-- back wall -->
    <rect x="307" y="386" width="579" height="334" fill="url(#fieldPhoto)" role="img" aria-label="Photo of a hand holding hemp leaves in a green field"/>
    <ellipse cx="500" cy="450" rx="95" ry="70" fill="url(#treeGlow)" role="img" aria-label="Tree with sky lightning bolts illustration"/>
    <text class="product-name" x="374" y="529" font-size="32">VERO BLOOM</text>
    <rect x="343" y="533" width="315" height="21" fill="var(--canopy-grey)"/>
    <text class="tagline" x="353" y="548" font-size="10.5">fast growth | vigorous roots | performance boost</text>
    <text class="promise" x="345" y="580" font-size="15">Your Best Choice For Fast</text>
    <text class="promise" x="345" y="598" font-size="15">Growth And Vitality!</text>
    <g class="benefit-icons">
      <circle cx="360" cy="641" r="10" fill="var(--sky-blue)"/>
      <text class="benefit-label" x="373" y="635" font-size="7.5">increased</text>
      <text class="benefit-label" x="373" y="643" font-size="7.5">nutrient</text>
      <text class="benefit-label" x="373" y="651" font-size="7.5">absorption</text>
      <circle cx="436" cy="641" r="10" fill="var(--sky-blue)"/>
      <text class="benefit-label" x="449" y="639" font-size="7.5">beneficial</text>
      <text class="benefit-label" x="449" y="647" font-size="7.5">microbes</text>
      <circle cx="518" cy="641" r="10" fill="var(--sky-blue)"/>
      <text class="benefit-label" x="531" y="639" font-size="7.5">plant</text>
      <text class="benefit-label" x="531" y="647" font-size="7.5">nutrition</text>
    </g>
    <rect x="307" y="722" width="579" height="12" fill="var(--band-orange)"/>

    <!-- side half walls -->
    <path d="M216,700 L302,598 L302,738 L216,808 Z" fill="var(--leaf-green)"/>
    <path d="M216,790 L302,725 L302,738 L216,808 Z" fill="var(--canopy-grey)"/>
    <path d="M898,598 L980,700 L980,808 L898,738 Z" fill="var(--leaf-green)"/>
    <path d="M898,725 L980,790 L980,808 L898,738 Z" fill="var(--canopy-grey)"/>
  </g>

  <!-- feather flag, left -->
  <g class="feather-flag">
    <rect x="71" y="300" width="4" height="525" fill="#1c1c1c"/>
    <path d="M73,800 L73,370 Q80,312 181,302 L181,690 Q160,760 73,800 Z" fill="var(--leaf-green)"/>
    <path d="M73,800 Q150,760 181,690" stroke="var(--band-orange)" stroke-width="7" fill="none"/>
    <text class="flag-word" x="128" y="338" text-anchor="middle">fast</text>
    <text class="flag-word" x="124" y="351" text-anchor="middle">growth</text>
    <line x1="98" y1="372" x2="176" y2="372" stroke="#f1f1f1" stroke-width="2"/>
    <text class="flag-word" x="128" y="397" text-anchor="middle">vigorous</text>
    <text class="flag-word" x="124" y="410" text-anchor="middle">roots</text>
    <line x1="92" y1="431" x2="176" y2="431" stroke="#f1f1f1" stroke-width="2"/>
    <text class="flag-word" x="128" y="456" text-anchor="middle">performance</text>
    <text class="flag-word" x="124" y="469" text-anchor="middle">boost</text>
    <rect x="113" y="497" width="40" height="252" fill="var(--canopy-grey)"/>
    <text class="product-name" font-size="26" text-anchor="middle" transform="translate(143,623) rotate(-90)">VERO BLOOM</text>
    <path d="M73,825 L10,885 M73,825 L135,885 M73,825 L73,870" stroke="#8a8a8a" stroke-width="2" fill="none"/>
  </g>

  <!-- feather flag, right -->
  <g class="feather-flag">
    <rect x="1113" y="300" width="4" height="525" fill="#1c1c1c"/>
    <path d="M1115,800 L1115,370 Q1108,312 1009,302 L1009,690 Q1030,760 1115,800 Z" fill="var(--leaf-green)"/>
    <path d="M1115,800 Q1040,760 1009,690" stroke="var(--band-orange)" stroke-width="7" fill="none"/>
    <text class="flag-word" x="1062" y="340" text-anchor="middle">fast</text>
    <text class="flag-word" x="1058" y="353" text-anchor="middle">growth</text>
    <line x1="1014" y1="376" x2="1094" y2="376" stroke="#f1f1f1" stroke-width="2"/>
    <text class="flag-word" x="1062" y="399" text-anchor="middle">vigorous</text>
    <text class="flag-word" x="1058" y="412" text-anchor="middle">roots</text>
    <line x1="1014" y1="433" x2="1100" y2="433" stroke="#f1f1f1" stroke-width="2"/>
    <text class="flag-word" x="1062" y="458" text-anchor="middle">performance</text>
    <text class="flag-word" x="1058" y="471" text-anchor="middle">boost</text>
    <rect x="1036" y="499" width="40" height="252" fill="var(--canopy-grey)"/>
    <text class="product-name" font-size="26" text-anchor="middle" transform="translate(1066,625) rotate(-90)">VERO BLOOM</text>
    <path d="M1115,825 L1052,885 M1115,825 L1178,885 M1115,825 L1115,870" stroke="#8a8a8a" stroke-width="2" fill="none"/>
  </g>

  <!-- table with runner -->
  <g class="display-table">
    <path d="M335,796 L897,796 L915,1018 L320,1018 Z" fill="var(--cloth-grey)"/>
    <rect x="529" y="796" width="202" height="222" fill="var(--sky-blue)"/>
    <rect x="548" y="796" width="164" height="222" fill="var(--leaf-green)"/>
    <ellipse cx="630" cy="885" rx="55" ry="42" fill="url(#treeGlow)" role="img" aria-label="Tree with sky lightning bolts illustration"/>
    <text class="product-name" x="630" y="934" font-size="19" text-anchor="middle">VERO BLOOM</text>
    <rect x="554" y="938" width="152" height="13" fill="var(--canopy-grey)"/>
    <text class="tagline" x="630" y="947.5" font-size="5.8" text-anchor="middle">fast growth | vigorous roots | performance boost</text>
    <rect x="595" y="968" width="3" height="42" fill="var(--text-white)"/>
    <text class="promise-soft" x="605" y="976" font-size="9">Your Best</text>
    <text class="promise-soft" x="605" y="987" font-size="9">Choice For</text>
    <text class="promise-accent" x="605" y="998" font-size="9">Fast Growth</text>
    <text class="promise-accent" x="605" y="1009" font-size="9">&amp; Vitality!</text>
  </g>

  <!-- ===== Scene two: corner view ===== -->
  <g class="booth-corner">
    <path d="M208,1446 Q480,1330 603,1170 Q740,1330 1000,1446 Z" fill="url(#roofShade)"/>
    <circle cx="436" cy="1355" r="15" fill="var(--leaf-green)"/>
    <text class="brand-name" x="458" y="1367" font-size="32">PELL VANTOR</text>

    <!-- front valance -->
    <rect x="205" y="1446" width="720" height="10" fill="var(--band-orange)"/>
    <rect x="205" y="1456" width="720" height="44" fill="var(--leaf-green)"/>
    <rect x="205" y="1500" width="720" height="40" fill="var(--canopy-grey)"/>
    <text class="product-name" x="277" y="1499" font-size="25">VERO BLOOM</text>
    <text class="tagline" x="269" y="1526" font-size="15">fast growth | vigorous roots | performance boost</text>
    <!-- side valance -->
    <path d="M925,1446 L1000,1478 L1000,1486 L925,1456 Z" fill="var(--band-orange)"/>
    <path d="M925,1456 L1000,1486 L1000,1530 L925,1500 Z" fill="var(--leaf-green)"/>
    <path d="M925,1500 L1000,1530 L1000,1565 L925,1540 Z" fill="var(--canopy-grey)"/>

    <!-- ceiling -->
    <rect x="599" y="1540" width="326" height="30" fill="var(--ceiling-grey)"/>

    <!-- legs -->
    <rect x="598" y="1540" width="6" height="250" fill="var(--pole-silver)"/>
    <rect x="992" y="1560" width="6" height="350" fill="var(--pole-silver)"/>

    <!-- back wall left half -->
    <rect x="216" y="1540" width="383" height="250" fill="url(#fieldPhoto)" role="img" aria-label="Photo of a hand holding hemp leaves in a green field"/>
    <ellipse cx="355" cy="1610" rx="80" ry="60" fill="url(#treeGlow)" role="img" aria-label="Tree with sky lightning bolts illustration"/>
    <text class="product-name" x="270" y="1708" font-size="24">VERO BLOOM</text>
    <rect x="243" y="1712" width="221" height="21" fill="var(--canopy-grey)"/>
    <text class="tagline" x="251" y="1726" font-size="7.6">fast growth | vigorous roots | performance boost</text>
    <text class="promise" x="247" y="1762" font-size="14">Your Best Choice For Fast</text>
    <text class="promise" x="247" y="1780" font-size="14">Growth And Vitality!</text>

    <!-- side half wall -->
    <rect x="606" y="1752" width="389" height="156" fill="var(--leaf-green)"/>
    <rect x="606" y="1888" width="389" height="20" fill="var(--canopy-grey)"/>

    <!-- front half wall -->
    <rect x="216" y="1788" width="697" height="225" fill="var(--leaf-green)"/>
    <rect x="216" y="1972" width="697" height="36" fill="var(--canopy-grey)"/>
    <ellipse cx="562" cy="1880" rx="110" ry="70" fill="url(#treeGlow)" role="img" aria-label="Tree with sky lightning bolts illustration"/>
    <text class="product-name" x="420" y="1966" font-size="42">VERO BLOOM</text>
    <rect x="386" y="1966" width="380" height="24" fill="var(--canopy-grey)"/>
    <text class="tagline" x="401" y="1983" font-size="13">fast growth | vigorous roots | performance boost</text>

    <!-- front legs -->
    <rect x="205" y="1540" width="7" height="480" fill="var(--pole-silver)"/>
    <rect x="915" y="1540" width="7" height="480" fill="var(--pole-silver)"/>
    <rect x="200" y="2017" width="18" height="4" fill="var(--canopy-grey-dark)"/>
    <rect x="910" y="2017" width="18" height="4" fill="var(--canopy-grey-dark)"/>
    <rect x="987" y="1908" width="16" height="4" fill="var(--canopy-grey-dark)"/>
  </g>

  <!-- ===== Full back wall ===== -->
  <text class="section-heading" x="613" y="2116" text-anchor="middle">Full Back Wall</text>
  <g class="back-wall">
    <rect x="226" y="2142" width="731" height="426" fill="url(#fieldPhoto)" role="img" aria-label="Photo of a hand holding hemp leaves in a green field"/>
    <ellipse cx="455" cy="2240" rx="125" ry="90" fill="url(#treeGlow)" role="img" aria-label="Tree with sky lightning bolts illustration"/>
    <text class="product-name" x="312" y="2334" font-size="44">VERO BLOOM</text>
    <rect x="271" y="2336" width="391" height="23" fill="var(--canopy-grey)"/>
    <text class="tagline" x="284" y="2352" font-size="14">fast growth | vigorous roots | performance boost</text>
    <text class="promise" x="274" y="2395" font-size="18">Your Best Choice For Fast</text>
    <text class="promise" x="274" y="2420" font-size="18">Growth And Vitality!</text>
    <g class="benefit-icons">
      <circle cx="292" cy="2471" r="12" fill="var(--sky-blue)"/>
      <text class="benefit-label" x="308" y="2463" font-size="9.5">increased</text>
      <text class="benefit-label" x="308" y="2473" font-size="9.5">nutrient</text>
      <text class="benefit-label" x="308" y="2483" font-size="9.5">absorption</text>
      <circle cx="390" cy="2471" r="12" fill="var(--sky-blue)"/>
      <text class="benefit-label" x="406" y="2469" font-size="9.5">beneficial</text>
      <text class="benefit-label" x="406" y="2479" font-size="9.5">microbes</text>
      <circle cx="491" cy="2471" r="12" fill="var(--sky-blue)"/>
      <text class="benefit-label" x="507" y="2469" font-size="9.5">plant</text>
      <text class="benefit-label" x="507" y="2479" font-size="9.5">nutrition</text>
    </g>
    <rect x="226" y="2572" width="731" height="14" fill="var(--band-orange)"/>
  </g>

  <!-- ===== Inside walls ===== -->
  <text class="section-heading" x="620" y="2654" text-anchor="middle">Inside Walls</text>
  <g class="inside-wall">
    <rect x="208" y="2668" width="781" height="204" fill="var(--leaf-green)"/>
    <rect x="208" y="2872" width="781" height="48" fill="var(--canopy-grey)"/>
    <ellipse cx="420" cy="2760" rx="115" ry="70" fill="url(#treeGlow)" role="img" aria-label="Tree with sky lightning bolts illustration"/>
    <text class="product-name" x="274" y="2862" font-size="40">VERO BLOOM</text>
    <rect x="240" y="2864" width="380" height="23" fill="var(--canopy-grey)"/>
    <text class="tagline" x="252" y="2880" font-size="13.5">fast growth | vigorous roots | performance boost</text>
    <rect x="718" y="2696" width="5" height="96" fill="var(--text-white)"/>
    <text class="promise-soft" x="745" y="2713" font-size="22">Your Best</text>
    <text class="promise-soft" x="745" y="2739" font-size="22">Choice For</text>
    <text class="promise-accent" x="745" y="2765" font-size="22">Fast Growth</text>
    <text class="promise-accent" x="745" y="2791" font-size="22">&amp; Vitality!</text>
    <g class="benefit-icons">
      <circle cx="690" cy="2843" r="12" fill="var(--sky-blue)"/>
      <text class="benefit-label" x="705" y="2835" font-size="9.5">increased</text>
      <text class="benefit-label" x="705" y="2845" font-size="9.5">nutrient</text>
      <text class="benefit-label" x="705" y="2855" font-size="9.5">absorption</text>
      <circle cx="792" cy="2843" r="12" fill="var(--sky-blue)"/>
      <text class="benefit-label" x="807" y="2841" font-size="9.5">beneficial</text>
      <text class="benefit-label" x="807" y="2851" font-size="9.5">microbes</text>
      <circle cx="903" cy="2843" r="12" fill="var(--sky-blue)"/>
      <text class="benefit-label" x="918" y="2841" font-size="9.5">plant</text>
      <text class="benefit-label" x="918" y="2851" font-size="9.5">nutrition</text>
    </g>
  </g>
</svg>
</body>
</html>
```